Dr Fobu smart screen Flyer design

Hi,

Please see attached file as I have done up a very very basic flyer just with the information that will need to be presented.

Please don't go with this as a format I would like, as I have no design skills at all.

I'm looking for something that is basic but professional looking capturing this information.
I would prefer if the symbols were changed so they were all consistent and the colour scheme worked together with the logo.

If you can use the picture of the screen provided as I will replace this once my product has its photoshoot.

Thanks!

```html
<!DOCTYPE html>
<html lang="en">
<head>
<meta charset="utf-8">
<title>Dr Fobu Smart Screen – HD LED Display Flyer</title>
<link rel="stylesheet" href="https://fonts.googleapis.com/css2?family=Great+Vibes&family=Montserrat:wght@300;400;500;600;700;800&display=swap">
<style>
  :root {
    --teal-light: #44a3b6;
    --teal-mid: #2d8398;
    --teal-dark: #1c5d6e;
    --yellow: #ffe81a;
    --white: #ffffff;
    --navy: #2a2961;
    --photo-earth: #8a6a3f;
    --photo-grass: #9a8a4a;
    --photo-sky: #a9c9dd;
    --photo-water: #3f8c8e;
    --badge-yellow: #f7d70c;
  }
  * { margin: 0; padding: 0; box-sizing: border-box; }
  html, body { width: 848px; height: 1200px; overflow: hidden; }
  body { font-family: "Montserrat", Arial, sans-serif; color: var(--white); }

  .flyer {
    position: relative;
    width: 848px;
    height: 1200px;
    overflow: hidden;
    background: radial-gradient(ellipse 70% 55% at 50% 45%, var(--teal-light) 0%, var(--teal-mid) 55%, var(--teal-dark) 100%);
  }

  .brand {
    position: absolute;
    left: 28px;
    top: 50px;
    display: flex;
    align-items: center;
    gap: 14px;
  }
  .brand-square { width: 28px; height: 28px; background: var(--white); }
  .brand-name {
    font-weight: 700;
    font-size: 50px;
    letter-spacing: 3px;
    color: var(--white);
    line-height: 1;
  }

  .hotline {
    position: absolute;
    right: 22px;
    top: 52px;
    text-align: center;
    color: var(--yellow);
    font-weight: 800;
    font-size: 27px;
    line-height: 1.3;
    letter-spacing: 1px;
  }

  .headline-script {
    position: absolute;
    left: 0; right: 0;
    top: 180px;
    text-align: center;
    font-family: "Great Vibes", cursive;
    font-weight: 400;
    font-size: 90px;
    line-height: 1;
    color: var(--white);
  }
  .headline-sub {
    position: absolute;
    left: 0; right: 0;
    top: 274px;
    text-align: center;
    font-weight: 500;
    font-size: 20px;
  }
  .headline-main {
    position: absolute;
    left: 0; right: 0;
    top: 308px;
    text-align: center;
    font-weight: 800;
    font-size: 61px;
    letter-spacing: 1px;
    color: var(--yellow);
    line-height: 1.05;
  }

  .showcase { position: absolute; left: 0; top: 360px; width: 848px; height: 560px; }

  .placement {
    position: absolute;
    left: 0; right: 0;
    top: 926px;
    text-align: center;
    color: var(--yellow);
    font-weight: 500;
    font-size: 17px;
    line-height: 22px;
  }
  .divider {
    position: absolute;
    left: 82px;
    top: 979px;
    width: 668px;
    height: 1px;
    background: var(--white);
    opacity: .85;
  }
  .cta {
    position: absolute;
    left: 0; right: 0;
    top: 994px;
    text-align: center;
    font-weight: 500;
    font-size: 22px;
    letter-spacing: .5px;
  }

  .features {
    position: absolute;
    left: 0;
    top: 1033px;
    width: 848px;
    height: 167px;
    background: var(--navy);
    display: flex;
  }
  .feature {
    flex: 1;
    text-align: center;
    padding-top: 18px;
  }
  .feature-icon { height: 30px; display: block; margin: 0 auto; }
  .feature-title {
    margin-top: 10px;
    font-weight: 700;
    font-size: 15.5px;
    letter-spacing: .5px;
  }
  .feature-text {
    margin-top: 14px;
    font-weight: 300;
    font-size: 13.5px;
    line-height: 17px;
    opacity: .9;
  }
</style>
</head>
<body>
<main class="flyer">

  <header class="brand">
    <span class="brand-square"></span>
    <span class="brand-name">Dr Fobu</span>
  </header>

  <div class="hotline">1300<br>DRFOBU</div>

  <h1 class="headline-script">Bring Attention</h1>
  <p class="headline-sub">to your business with your own custom built</p>
  <h2 class="headline-main">HD LED DISPLAY</h2>

  <svg class="showcase" viewBox="0 360 848 560" width="848" height="560">
    <defs>
      <linearGradient id="tiger-scene" x1="0" y1="0" x2="1" y2="1">
        <stop offset="0" stop-color="var(--photo-earth)"/>
        <stop offset=".55" stop-color="var(--photo-grass)"/>
        <stop offset="1" stop-color="#5e4a2c"/>
      </linearGradient>
      <linearGradient id="lake-scene" x1="0" y1="0" x2="0" y2="1">
        <stop offset="0" stop-color="#6f9fc3"/>
        <stop offset=".45" stop-color="var(--photo-sky)"/>
        <stop offset=".55" stop-color="#6d8580"/>
        <stop offset="1" stop-color="var(--photo-water)"/>
      </linearGradient>
    </defs>

    <polyline class="frame-lines" points="303,412 739,412 739,907 116,907 116,850"
              stroke="var(--white)" stroke-width="1.5" fill="none" opacity=".9"/>

    <rect class="product-photo" role="img"
          aria-label="Product photo: large LED screen showing a tiger in dry grass before rocks"
          x="82" y="368" width="454" height="477" fill="url(#tiger-scene)"/>

    <circle class="quality-badge" cx="536" cy="506" r="45" fill="var(--badge-yellow)"/>

    <rect class="product-photo" role="img"
          aria-label="Product photo: smaller LED screen showing a mountain lake reflecting the sky"
          x="429" y="537" width="318" height="331" fill="url(#lake-scene)"/>
  </svg>

  <p class="placement">Our displays can be mounted outdoors on walls, roofs, fixed signs, trailer etc.<br>We also do indoor LED screens for shop fronts and display stands.</p>
  <div class="divider"></div>
  <p class="cta">GET A FREE QUOTE www.drfobuscreens.com.au</p>

  <section class="features">
    <div class="feature">
      <svg class="feature-icon" viewBox="0 0 60 30" width="60" height="30">
        <g fill="none" stroke="var(--white)" stroke-width="1.6" stroke-linecap="round">
          <path d="M12,8 Q7,15 12,22"/><path d="M7,5 Q0,15 7,25"/>
          <path d="M48,8 Q53,15 48,22"/><path d="M53,5 Q60,15 53,25"/>
        </g>
        <text x="30" y="21" text-anchor="middle" font-family="Montserrat, sans-serif" font-size="14" font-weight="500" fill="var(--white)">4G</text>
      </svg>
      <h3 class="feature-title">4G/WIFI CAPABLE</h3>
      <p class="feature-text">Change screen content with a PC,<br>tablet or mobile with an easy-to-use<br>app anywhere in the world</p>
    </div>
    <div class="feature">
      <svg class="feature-icon" viewBox="0 0 30 30" width="30" height="30">
        <g stroke="var(--white)" stroke-width="1.8" fill="none" stroke-linecap="round">
          <path d="M3,8 H15 M9,2 V14 M5,4 L13,12 M13,4 L5,12"/>
          <path d="M19,6 a3,3 0 0 1 6,0 V19 a5,5 0 1 1 -6,0 Z"/>
          <line x1="22" y1="12" x2="22" y2="22"/>
        </g>
      </svg>
      <h3 class="feature-title">ONLINE MONITORING</h3>
      <p class="feature-text">Monitor cabinet humidity,<br>temperature &amp; more in real time<br>online. Receive alerts via Email.</p>
    </div>
    <div class="feature">
      <svg class="feature-icon" viewBox="0 0 30 30" width="30" height="30">
        <circle cx="15" cy="15" r="6" fill="none" stroke="var(--white)" stroke-width="1.8"/>
        <path d="M15,9 A6,6 0 0 1 15,21 Z" fill="var(--white)"/>
        <g stroke="var(--white)" stroke-width="1.8" stroke-linecap="round">
          <path d="M15,1 V5 M15,25 V29 M1,15 H5 M25,15 H29 M5,5 L8,8 M22,22 L25,25 M25,5 L22,8 M8,22 L5,25"/>
        </g>
      </svg>
      <h3 class="feature-title">INTELLIGENT BRIGHTNESS</h3>
      <p class="feature-text">Screen will automatically adjust<br>to suit ambient light, improving view<br>quality &amp; saving power.</p>
    </div>
  </section>

</main>
</body>
</html>
```